SEO AND WEB DESIGN COMPANY BUSINESS CARD DESIGN

I need an eye catching , simple business card design that will match my logo . I need 2 versions of it ( white background and black background) - SOME PEOPLE DID NOT GET IT AND SENDING US FRONT WHITE BACK WHITE VERSIONS WHICH IS NOT CORRECT.

ONE VERSION SHOULD BE BACK AND FRONT ALL BLACK , SECOND VERSION SHOULD BE BACK AND FRONT ALL WHITE

logo psd files are attached for both versions. The business card is going to have : First Name- Last name - position - phone numbers

```html
<!DOCTYPE html>
<html lang="en">
<head>
<meta charset="utf-8">
<title>Northway Digital — Business Cards</title>
<link href="https://fonts.googleapis.com/css2?family=Oswald:wght@500;600&family=Roboto:wght@400;500&display=swap" rel="stylesheet">
<style>
  :root {
    --backdrop: #2b2b2d;
    --card-black: #0b0b0c;
    --card-white: #ffffff;
    --ink: #111111;
    --logo-grey: #6f7073;
    --accent-blue: #3f7cc8;
    --link-blue: #2f5fa6;
  }
  html, body {
    margin: 0;
    width: 1200px;
    height: 942px;
    overflow: hidden;
    background: var(--backdrop);
  }
  .stage {
    position: relative;
    width: 1200px;
    height: 942px;
  }
  .card {
    position: absolute;
    top: 200px;
    width: 340px;
    height: 540px;
    border-radius: 28px;
    box-sizing: border-box;
    overflow: hidden;
  }
  .card--black {
    left: 200px;
    background: var(--card-black);
  }
  .card--white {
    left: 640px;
    background: var(--card-white);
  }
  .brand {
    position: absolute;
    display: flex;
    writing-mode: vertical-rl;
    align-items: center;
    gap: 12px;
    font-family: "Oswald", sans-serif;
    font-weight: 600;
    letter-spacing: 1px;
    text-transform: uppercase;
    line-height: 1;
  }
  .brand__mark {
    width: 14px;
    height: 14px;
    background: var(--accent-blue);
  }
  .card--black .brand {
    left: 135px;
    top: 110px;
    font-size: 56px;
    color: var(--logo-grey);
  }
  .card--white .brand {
    left: 48px;
    top: 60px;
    font-size: 40px;
    color: var(--ink);
  }
  .contact {
    position: absolute;
    right: 36px;
    top: 240px;
    writing-mode: vertical-rl;
    display: flex;
    flex-direction: column;
    gap: 6px;
    font-family: "Roboto", sans-serif;
    font-size: 15px;
    color: var(--ink);
  }
  .contact__name {
    font-family: "Oswald", sans-serif;
    font-weight: 600;
    font-size: 28px;
    line-height: 1;
    text-transform: uppercase;
  }
  .contact__title {
    font-family: "Oswald", sans-serif;
    font-weight: 500;
    font-size: 14px;
    color: var(--accent-blue);
    text-transform: uppercase;
    margin-inline-end: 4px;
  }
  .contact__line {
    display: flex;
    align-items: center;
    gap: 6px;
  }
  .contact__line svg {
    width: 12px;
    height: 12px;
    fill: var(--link-blue);
  }
  .contact__web {
    color: var(--link-blue);
    margin-top: 14px;
  }
</style>
</head>
<body>
<main class="stage">
  <section class="card card--black" aria-label="Black business card">
    <div class="brand"><span class="brand__mark"></span>Northway Digital</div>
  </section>

  <section class="card card--white" aria-label="White business card">
    <div class="brand"><span class="brand__mark"></span>Northway Digital</div>
    <div class="contact">
      <div class="contact__name">Your Name</div>
      <div class="contact__title">Job Title</div>
      <div class="contact__line">
        <svg viewBox="0 0 12 12" aria-hidden="true"><rect x="3" y="0" width="6" height="12" rx="1.5"/></svg>
        <span>000 000 0000</span>
      </div>
      <div class="contact__line">
        <svg viewBox="0 0 12 12" aria-hidden="true"><path d="M2 1 L4.5 1 L5.5 3.5 L4 4.8 Q5 7 7.2 8 L8.5 6.5 L11 7.5 L11 10 Q10 11 8.5 11 Q2 9.5 1 3.5 Q1 2 2 1 Z"/></svg>
        <span>000 000 0000</span>
      </div>
      <div class="contact__line">
        <svg viewBox="0 0 12 12" aria-hidden="true"><rect x="0" y="2" width="12" height="9" rx="1"/></svg>
        <span>youremail@xyz.com</span>
      </div>
      <div class="contact__web">www.yourwebsite.com</div>
    </div>
  </section>
</main>
</body>
</html>
```